Harbin Vale Co Tank Lining Services

I would check out our website for an a quick understanding of what Blasting and Painting "is". www.harbinvaleco.example

I need to Design "sales postcard" or "company postcard" that outlines the TANK LINING division of our company. (What is a "tank lining"? It is a coating applied to the interior of a Water Tank or "Water Tower". There are certifications and special equipment needed to provide these services that make it a unique market) This is a NEW service we are offing to our customers.

We want to include photo's of: Sand Blasting, Painting, and Welding on a Ground Storage Tank. (please see attached)

Bullet points to include:
-Critical Areas
-Tank Inspections
-Manway Installation
-Fire/Domestic Water

Please Note: a little says a lot in regards to regards to data crammed into "postcards". Our market is one that won't need to be "spoon" fed. I need potential clients to read the name and our contact info (obviously).

Target Market(s)

Building Owners

Industry/Entity Type

Construction

Font styles to use
Sans Serif

Colors
0054AA
0677BA
7BADD7
CADEEF
E8F1F8

Requirements
Must have
• Layered photos or pictures
Nice to have
• Cropped Layered photos are good
Should not have
• to much clutter

```html
<!DOCTYPE html>
<html lang="en">
<head>
<meta charset="utf-8">
<title>Harbin Vale Co – Tank Lining Postcard</title>
<link href="https://fonts.googleapis.com/css2?family=Montserrat:wght@400;500;600;700;800&display=swap" rel="stylesheet">
<style>
:root{
  --blue-deep:#0054AA;
  --blue-mid:#0677BA;
  --blue-soft:#7BADD7;
  --blue-pale:#CADEEF;
  --blue-mist:#E8F1F8;
  --ink:#111111;
  --text:#333333;
  --grey-pill:#6b6b6b;
  --band-dark:#1f1f1f;
  --stage:#efefef;
  --white:#ffffff;
  --rule:#9a9a9a;
}
*{margin:0;padding:0;box-sizing:border-box}
html,body{width:783px;height:1200px;overflow:hidden;background:var(--stage);font-family:'Montserrat',sans-serif}
.postcard{position:absolute;left:51px;width:680px;height:452px;background:var(--white);overflow:hidden;box-shadow:0 2px 6px rgba(0,0,0,.18)}
.postcard--front{top:40px}
.postcard--back{top:540px}

/* front */
.hero-photo{position:absolute;left:290px;top:0;width:390px;height:378px;
  background:linear-gradient(180deg,#5f7fb0 0%,#9aa7c4 30%,#d9a38f 48%,#8c9bb5 62%,#51627c 80%,#4d6a3c 100%)}
.hero-fade{position:absolute;left:0;top:0;width:520px;height:378px;
  background:linear-gradient(90deg,var(--white) 0%,var(--white) 52%,rgba(255,255,255,.85) 68%,rgba(255,255,255,0) 100%)}
.brand{position:absolute;display:flex;align-items:center;gap:8px;font-weight:700;color:var(--blue-deep)}
.brand__mark{width:16px;height:16px;background:var(--blue-deep)}
.postcard--front .brand{left:28px;top:36px;font-size:22px}
.focus-kicker{position:absolute;left:28px;top:96px;font-size:26px;font-weight:700;color:var(--ink);letter-spacing:-.5px}
.focus-title{position:absolute;left:28px;top:124px;font-size:45px;font-weight:800;color:var(--blue-deep);letter-spacing:-1px}
.focus-rule{position:absolute;left:28px;top:176px;width:350px;height:1px;background:var(--rule)}
.focus-rule::after{content:"";position:absolute;left:34px;top:-1.5px;width:50px;height:4px;background:var(--blue-deep);border-radius:2px}
.tagline{position:absolute;left:28px;top:190px;font-size:19px;font-weight:600;line-height:24px;color:var(--ink)}
.services-pill{position:absolute;left:31px;top:252px;width:180px;height:34px;background:var(--grey-pill);border-radius:0 17px 17px 0;
  color:var(--white);font-size:18px;font-weight:700;letter-spacing:.5px;line-height:34px;padding-left:16px}
.service-list{position:absolute;left:28px;top:300px;width:380px;display:grid;grid-template-columns:165px 215px;row-gap:10px;list-style:none}
.service-list li{display:flex;align-items:center;gap:6px;font-size:15px;font-weight:600;color:var(--ink)}
.service-icon{width:26px;height:26px;flex:none}
.contact-band{position:absolute;left:0;top:384px;width:680px;height:68px;background:var(--blue-deep);display:flex;align-items:center;gap:28px;padding-left:32px;color:var(--white);font-weight:700}
.contact-band .phone{font-size:28px;display:flex;align-items:center;gap:10px}
.contact-band .web{font-size:24px;display:flex;align-items:center;gap:10px}

/* back */
.about-title{position:absolute;left:28px;top:30px;font-size:20px;font-weight:700;color:var(--blue-deep)}
.about-copy{position:absolute;left:28px;top:60px;width:346px;font-size:8.2px;line-height:11px;color:var(--text);text-align:justify}
.about-copy p{margin-bottom:10px}
.gallery-band{position:absolute;left:0;top:236px;width:380px;height:138px;background:var(--band-dark);clip-path:polygon(0 0,100% 0,91% 100%,0 100%)}
.gallery-tile{position:absolute;top:22px;width:116px;height:94px;clip-path:polygon(10% 0,100% 0,90% 100%,0 100%)}
.gallery-tile--blast{left:-12px;background:linear-gradient(135deg,#a59c74,#6e6a55 60%,#8a3a36)}
.gallery-tile--paint{left:110px;background:linear-gradient(135deg,#d9c3a0,#b54b3a 45%,#2c5a8c)}
.gallery-tile--weld{left:232px;background:linear-gradient(180deg,#2b6fc0,#9cc3e8 55%,#d9d9d9)}
.gallery-label{position:absolute;top:94px;width:100px;height:22px;background:rgba(90,90,90,.9);color:var(--white);font-size:6.5px;font-weight:700;display:flex;align-items:center;justify-content:center;text-align:center;line-height:7px}
.back-contact{position:absolute;left:0;top:376px;width:410px;height:76px;background:var(--blue-deep);clip-path:polygon(0 0,85% 0,100% 100%,0 100%);color:var(--white);font-weight:700;padding:12px 0 0 34px}
.back-contact div{display:flex;align-items:center;gap:9px;line-height:25px}
.back-contact .phone{font-size:20px}
.back-contact .web{font-size:19px}
.postcard--back .brand{left:420px;top:48px;font-size:17px}
.stamp-box{position:absolute;left:592px;top:22px;width:66px;height:78px;background:#e6e6e6}
.address-line{position:absolute;left:420px;width:234px;height:1px;background:var(--rule)}
.spray-photo{position:absolute;left:540px;top:336px;width:140px;height:116px;
  background:radial-gradient(ellipse at 60% 70%,#1d5fc2 0%,#5c8fd4 35%,rgba(255,255,255,0) 70%)}
</style>
</head>
<body>

<section class="postcard postcard--front" aria-label="Postcard front">
  <div class="hero-photo" role="img" aria-label="Refinery and storage plant at dusk under a pink and blue sky"></div>
  <div class="hero-fade"></div>
  <div class="brand"><span class="brand__mark"></span>Harbin Vale Co</div>
  <p class="focus-kicker">OUR FOCUS IS ON</p>
  <h1 class="focus-title">CUSTOMER CARE</h1>
  <div class="focus-rule"></div>
  <p class="tagline">We Are Fully Equipped To Do<br>The Heavy Lifting For You</p>
  <div class="services-pill">OUR SERVICES</div>
  <ul class="service-list">
    <li><svg class="service-icon" viewBox="0 0 26 26"><circle cx="13" cy="13" r="13" fill="var(--blue-deep)"/><path d="M7 18h12M9 18v-6h3v6M14 18v-9h3v9" stroke="#fff" stroke-width="1.5" fill="none"/></svg>Critical Areas</li>
    <li><svg class="service-icon" viewBox="0 0 26 26"><circle cx="13" cy="13" r="13" fill="var(--blue-deep)"/><circle cx="13" cy="13" r="5" stroke="#fff" stroke-width="1.5" fill="none"/><circle cx="13" cy="13" r="1.5" fill="#fff"/></svg>Manway Installation</li>
    <li><svg class="service-icon" viewBox="0 0 26 26"><circle cx="13" cy="13" r="13" fill="var(--blue-deep)"/><rect x="7" y="10" width="12" height="8" rx="2" stroke="#fff" stroke-width="1.5" fill="none"/><path d="M7 13h12" stroke="#fff" stroke-width="1.2"/></svg>Tank Inspections</li>
    <li><svg class="service-icon" viewBox="0 0 26 26"><circle cx="13" cy="13" r="13" fill="var(--blue-deep)"/><path d="M13 6c3 4 5 6.5 5 9a5 5 0 0 1-10 0c0-2.5 2-5 5-9z" stroke="#fff" stroke-width="1.5" fill="none"/></svg>Fire/Domestic Water</li>
  </ul>
  <div class="contact-band">
    <span class="phone"><svg width="22" height="22" viewBox="0 0 24 24"><path d="M6.6 10.8a15 15 0 0 0 6.6 6.6l2.2-2.2a1 1 0 0 1 1-.25 11.4 11.4 0 0 0 3.6.57 1 1 0 0 1 1 1V20a1 1 0 0 1-1 1A17 17 0 0 1 3 4a1 1 0 0 1 1-1h3.5a1 1 0 0 1 1 1c0 1.25.2 2.45.57 3.57a1 1 0 0 1-.25 1z" fill="none" stroke="#fff" stroke-width="1.6"/></svg>(555) 014-2290</span>
    <span class="web"><svg width="20" height="20" viewBox="0 0 24 24" fill="none" stroke="#fff" stroke-width="1.6"><circle cx="12" cy="12" r="9"/><path d="M3 12h18M12 3c3 3 3 15 0 18M12 3c-3 3-3 15 0 18"/></svg>www.harbinvaleco.example</span>
  </div>
</section>

<section class="postcard postcard--back" aria-label="Postcard back">
  <h2 class="about-title">ABOUT US</h2>
  <div class="about-copy">
    <p>At Harbin Vale Co, we have only one purpose – satisfying you and your needs for protective coating services.</p>
    <p>It all started in 2008 with Martin Ellery's vision to provide the best industrial coatings and services to Houston-area companies. To achieve his vision, Martin assembled a team of experienced industrial coatings professionals who shared his belief that business is built on customer satisfaction driven by quality, responsiveness and value. Since that time, Harbin Vale has grown and expanded to become a premier industrial coating &amp; services firm.</p>
    <p>Today, we are proud to be the supplier of choice for many of the world's leading energy companies, oil and gas firms, and petrochemical concerns...</p>
  </div>
  <div class="gallery-band">
    <div class="gallery-tile gallery-tile--blast" role="img" aria-label="Worker sand blasting steel inside a tank"></div>
    <div class="gallery-tile gallery-tile--paint" role="img" aria-label="Paint brushes and open paint cans"></div>
    <div class="gallery-tile gallery-tile--weld" role="img" aria-label="Ground storage tanks under a blue sky"></div>
    <span class="gallery-label" style="left:2px">SAND BLASTING</span>
    <span class="gallery-label" style="left:124px">PAINTING</span>
    <span class="gallery-label" style="left:246px">WELDING ON A<br>GROUND STORAGE TANK</span>
  </div>
  <div class="back-contact">
    <div class="phone"><svg width="16" height="16" viewBox="0 0 24 24"><path d="M6.6 10.8a15 15 0 0 0 6.6 6.6l2.2-2.2a1 1 0 0 1 1-.25 11.4 11.4 0 0 0 3.6.57 1 1 0 0 1 1 1V20a1 1 0 0 1-1 1A17 17 0 0 1 3 4a1 1 0 0 1 1-1h3.5a1 1 0 0 1 1 1c0 1.25.2 2.45.57 3.57a1 1 0 0 1-.25 1z" fill="none" stroke="#fff" stroke-width="1.8"/></svg>(555) 014-2290</div>
    <div class="web"><svg width="15" height="15" viewBox="0 0 24 24" fill="none" stroke="#fff" stroke-width="1.8"><circle cx="12" cy="12" r="9"/><path d="M3 12h18M12 3c3 3 3 15 0 18M12 3c-3 3-3 15 0 18"/></svg>www.harbinvaleco.example</div>
  </div>
  <div class="brand"><span class="brand__mark"></span>Harbin Vale Co</div>
  <div class="stamp-box"></div>
  <div class="address-line" style="top:156px"></div>
  <div class="address-line" style="top:194px"></div>
  <div class="address-line" style="top:232px"></div>
  <div class="address-line" style="top:272px"></div>
  <div class="spray-photo" role="img" aria-label="Gloved hand holding a paint spray gun"></div>
</section>

</body>
</html>
```